Wholesale Fashion Agent

Industry/Entity Type

Fashion

Contact Information for Business Card

I have attached the previous logo, we are wanting to re-vamp with black and white only. Sharp and more modern.

Marisa Tolkett Agencies back of card
address (to be advised, as we are moving)

MT Agencies front of card, with Fashion Agent on the front

```html
<!DOCTYPE html>
<html lang="en">
<head>
<meta charset="utf-8">
<title>Marisa Tolkett Agencies – Business Card Options</title>
<link rel="stylesheet" href="https://fonts.googleapis.com/css2?family=Cinzel:wght@400;500&family=Josefin+Sans:wght@400&family=Tinos:wght@400&display=swap">
<style>
  :root {
    --board: #e6e6e6;
    --ink: #151515;
    --paper: #ffffff;
    --ghost: #ececec;
    --label: #1a1a1a;
  }
  * { margin: 0; padding: 0; box-sizing: border-box; }
  html, body { width: 1200px; height: 887px; overflow: hidden; background: var(--board); }
  .board { position: relative; width: 1200px; height: 887px; }

  .option-label {
    position: absolute; top: 28px; width: 40px; margin-left: -20px;
    text-align: center; font: 400 26px/30px "Josefin Sans", sans-serif; color: var(--label);
  }

  .card {
    position: absolute; width: 533px; height: 328px; background: var(--paper);
    overflow: hidden; box-shadow: 0 6px 12px rgba(0,0,0,0.25);
  }
  .col-1 { left: 29px; }
  .col-2 { left: 625px; }
  .front { top: 107px; }
  .back  { top: 494px; }

  /* Bands */
  .band { position: absolute; left: 0; width: 100%; background: var(--ink); }
  .front .band-main { top: 0; height: 94px; }
  .front .band-rule { top: 97px; height: 5px; }
  .back .band-rule { top: 221px; height: 6px; }
  .back .band-main { top: 230px; height: 98px; }

  /* Monogram block: name set in text font inside a plain square */
  .mark {
    position: absolute; background: var(--ink); border: 3px solid var(--paper);
    outline: 2px solid var(--ink);
    display: flex; align-items: center; justify-content: center;
    font-family: "Cinzel", serif; font-weight: 500; color: var(--paper); letter-spacing: 1px;
  }
  .front.col-1 .mark { left: 224px; top: 61px; width: 88px; height: 86px; font-size: 36px; }
  .front.col-2 .mark { left: 231px; top: 68px; width: 74px; height: 73px; font-size: 30px; }
  .back .mark { left: 240px; top: 205px; width: 54px; height: 54px; font-size: 21px; }

  .name {
    position: absolute; left: 0; width: 100%; text-align: center;
    font: 400 33px/1 "Cinzel", serif; color: var(--ink); letter-spacing: 0.5px;
  }
  .role {
    position: absolute; left: 0; width: 100%; text-align: center;
    font: 400 19px/1 "Josefin Sans", sans-serif; letter-spacing: 4px; color: var(--ink);
  }
  .col-1 .name { top: 178px; }
  .col-1 .role { top: 224px; }
  .col-2 .name { top: 157px; }
  .col-2 .role { top: 201px; }

  /* Back */
  .ghost-mark {
    position: absolute; left: 325px; top: -6px;
    font: 400 200px/1 "Cinzel", serif; color: var(--ghost);
  }
  .company {
    position: absolute; left: 0; width: 100%; top: 28px; text-align: center;
  }
  .company span {
    font: 400 21px/1 "Cinzel", serif; color: var(--ink);
    border-bottom: 1.5px solid var(--ink); padding-bottom: 2px;
  }
  .contacts { position: absolute; left: 73px; top: 70px; list-style: none; }
  .contacts li {
    display: flex; align-items: center; height: 25.5px;
    font: 400 16.5px/1 "Tinos", serif; color: var(--ink);
  }
  .contacts svg { width: 15px; height: 15px; margin-right: 6px; flex: none; }
  .website {
    position: absolute; left: 0; width: 100%; top: 279px; text-align: center;
    font: 400 18.5px/1 "Tinos", serif; color: var(--paper); letter-spacing: 0.5px;
  }
</style>
</head>
<body>
<svg width="0" height="0" style="position:absolute" aria-hidden="true">
  <symbol id="icon-phone" viewBox="0 0 16 16"><path d="M4 1.5 6 4 4.8 5.6c.7 1.9 2.1 3.4 4 4.3L10.4 8.6 13 10.5l-.8 2.7c-.3.7-1 1-1.8.8C6 12.7 2.6 9 1.8 4.4c-.1-.8.3-1.5 1-1.8z" fill="#151515"/></symbol>
  <symbol id="icon-mobile" viewBox="0 0 16 16"><rect x="4" y="1" width="8" height="14" rx="1.5" fill="none" stroke="#151515" stroke-width="1.4"/><line x1="6.5" y1="12.6" x2="9.5" y2="12.6" stroke="#151515" stroke-width="1.2"/></symbol>
  <symbol id="icon-fax" viewBox="0 0 16 16"><rect x="4" y="1.5" width="8" height="5" fill="none" stroke="#151515" stroke-width="1.2"/><rect x="1" y="6.5" width="14" height="6" rx="1" fill="none" stroke="#151515" stroke-width="1.2"/><rect x="4" y="10" width="8" height="4.5" fill="#fff" stroke="#151515" stroke-width="1.2"/></symbol>
  <symbol id="icon-mail" viewBox="0 0 16 16"><rect x="1" y="3.5" width="14" height="9" fill="none" stroke="#151515" stroke-width="1.3"/><path d="M1 3.5 8 9l7-5.5M1 12.5l5-4.5m9 4.5-5-4.5" fill="none" stroke="#151515" stroke-width="1.1"/></symbol>
  <symbol id="icon-home" viewBox="0 0 16 16"><path d="M1 7 8 2l7 5v1.5H1z" fill="#151515"/><rect x="2.5" y="8.5" width="11" height="6" fill="#151515"/><rect x="6.5" y="10" width="3" height="4.5" fill="#fff"/></symbol>
</svg>

<main class="board">
  <div class="option-label" style="left:280px">1</div>
  <div class="option-label" style="left:890px">2</div>

  <!-- Option 1 front -->
  <section class="card front col-1">
    <div class="band band-main"></div>
    <div class="band band-rule"></div>
    <div class="mark">MT</div>
    <h1 class="name">Marisa Tolkett</h1>
    <p class="role">FASHION AGENT</p>
  </section>

  <!-- Option 2 front -->
  <section class="card front col-2">
    <div class="band band-main"></div>
    <div class="band band-rule"></div>
    <div class="mark">MT</div>
    <h1 class="name">Marisa Tolkett</h1>
    <p class="role">FASHION AGENT</p>
  </section>

  <!-- Option 1 back -->
  <section class="card back col-1">
    <div class="ghost-mark" aria-hidden="true">MT</div>
    <h2 class="company"><span>Marisa Tolkett Agencies</span></h2>
    <ul class="contacts">
      <li><svg><use href="#icon-phone"/></svg>07-3210 4476</li>
      <li><svg><use href="#icon-mobile"/></svg>0412 587 630</li>
      <li><svg><use href="#icon-fax"/></svg>07-3210 4480</li>
      <li><svg><use href="#icon-mail"/></svg>marisa@mtagencies.com.au</li>
      <li><svg><use href="#icon-home"/></svg>Unit 4/9 Harlow Street West End QLD 4101</li>
    </ul>
    <div class="band band-rule"></div>
    <div class="band band-main"></div>
    <div class="mark">MT</div>
    <p class="website">WWW.MTAGENCIES.COM.AU</p>
  </section>

  <!-- Option 2 back -->
  <section class="card back col-2">
    <h2 class="company"><span>Marisa Tolkett Agencies</span></h2>
    <ul class="contacts">
      <li><svg><use href="#icon-phone"/></svg>07-3210 4476</li>
      <li><svg><use href="#icon-mobile"/></svg>0412 587 630</li>
      <li><svg><use href="#icon-fax"/></svg>07-3210 4480</li>
      <li><svg><use href="#icon-mail"/></svg>marisa@mtagencies.com.au</li>
      <li><svg><use href="#icon-home"/></svg>Unit 4/9 Harlow Street West End QLD 4101</li>
    </ul>
    <div class="band band-rule"></div>
    <div class="band band-main"></div>
    <div class="mark">MT</div>
    <p class="website">WWW.MTAGENCIES.COM.AU</p>
  </section>
</main>
</body>
</html>
```